WP website design (Dorlen Group)

We need a wordpress design for an established auction and real estate company based in Kansas. The winning design will incorporate a professional color scheme with company logo in a clean layout with specified widgets. The design needs to consider that this will be developed on a responsive theme. Colors are blue and gray, with perhaps black or other as an accent/highlight color.

Must Have:
- Navigation:
1) Home 2) Auctions 3) Real Estate Listings 4) Rentals 5) Our Team 6) Services 7) Past Auctions 8) Testimonials 9) Contact Us

Page will have large slideshow, please use either image provided as the initial slide. Homepage will have auctions - as at http://brindlebidhouse.com/upcoming-auctions/. Home page will also have 2 calls to action: "NOTIFY ME OF UPCOMING AUCTIONS" (newsletter signup), and "I AM READY TO SELL. PLEASE CONTACT ME FOR A FREE CONSULTATION." with an email button.

Footer will have smaller company logo, credit card logo, and attached association logos and this contact info:
.(555) 318-7061: OFFICE
(555) 318-7095: FAX
dgroup@vrbx.com: email
Address: 718 N. Elm Ave., Johnson KS
Mailing Address: PO Box 927, Harlow, NE

Widgets:
1) email sign up 2) Social media (twitter, FB, linked-in, pinterest) 3) Mortgage calculator 4) testimonials blog

Nice to Have:
- demonstrate the drop-down menu styling, e.g. under Auctions
Auction Calendar
4 Key Auction Methods
Auction Benefits

Industry/Entity Type

Real Estate

Font styles to use
Sans Serif

Colors

Designer to choose colors to be used in the design.

Requirements
Must have
• - Navigation:

.(555) 318-7061: OFFICE
(555) 318-7095: FAX
dgroup@vrbx.com: email

Widgets:
Nice to have
• Nice to Have:
Auction Calendar
4 Key Auction Methods
Auction Benefits

```html
<!DOCTYPE html>
<html lang="en">
<head>
<meta charset="utf-8">
<title>The Dorlen Group</title>
<link href="https://fonts.googleapis.com/css2?family=Noto+Serif:ital,wght@0,400;0,700;1,400&family=Open+Sans:wght@400;600;700&display=swap" rel="stylesheet">
<style>
:root{
  --blue:#2456a6;
  --blue-dark:#1b4488;
  --gold:#e8b422;
  --gold-dark:#d49d12;
  --gray-bg:#f3f3f3;
  --text:#444;
  --head:#2c5594;
}
*{box-sizing:border-box;margin:0;padding:0}
html,body{width:798px;height:1200px;overflow:hidden}
body{position:relative;background:#fff;font-family:"Open Sans",sans-serif;color:var(--text)}
.abs{position:absolute}

/* header */
.logo{left:109px;top:24px;display:flex;align-items:center;gap:8px}
.logo-mark{width:34px;height:34px;border-radius:50%;border:5px solid var(--blue)}
.logo-name{font-family:"Noto Serif",serif;font-size:26px;color:var(--blue);line-height:1;white-space:nowrap}
.social{left:586px;top:18px;display:flex;gap:6px}
.social span{width:22px;height:22px;border-radius:3px;background:var(--blue)}
.social span:last-child{background:#c9463a}
.call{left:528px;top:53px;font-size:15px;color:#7b8fae}
.call b{color:var(--blue);font-weight:400}

/* nav */
.nav{left:0;top:86px;width:798px;height:31px;background:linear-gradient(#2f63b3,#1f4d99);border-bottom:1px solid #173f80}
.nav ul{position:absolute;left:106px;top:0;display:flex;list-style:none;height:31px;border-left:1px solid #3f72c0}
.nav li{height:31px;line-height:31px;text-align:center;font-family:"Noto Serif",serif;font-size:8.6px;font-weight:700;color:#fff;border-right:1px solid #3f72c0;white-space:nowrap}
.nav li.active{background:#1a4283}
.dropdown{left:164px;top:117px;width:110px;height:62px;background:var(--blue);padding:6px 0 0 10px;z-index:3}
.dropdown p{font-size:7.6px;color:#fff;line-height:17.5px}

/* hero */
.hero{left:0;top:117px;width:798px;height:247px;background:linear-gradient(180deg,#c9d3d6 0%,#b9bd9e 28%,#7d8a4f 45%,#4f6a2c 70%,#3b5422 100%)}
.hero-title{left:152px;top:202px;font-family:"Noto Serif",serif;font-weight:400;font-size:19.5px;line-height:26px;color:#fff}
.hero-title em{font-style:normal;color:#e9d33a}
.calc{left:505px;top:130px;width:187px;height:220px;background:#fff;box-shadow:0 1px 4px rgba(0,0,0,.25)}
.calc-head{height:37px;background:#aab1bc;color:#fff;font-family:"Noto Serif",serif;font-weight:700;font-size:14px;line-height:37px;text-align:center}
.calc-note{left:13px;top:44px;font-size:7.4px;line-height:12.5px;color:#777;width:160px}
.field{height:20px;border:1px solid #ddd;font-size:7.4px;color:#888;line-height:18px;padding-left:7px}
.select-arrow{position:absolute;right:0;top:0;width:18px;height:18px;border-left:1px solid #ddd;text-align:center;font-size:6px;line-height:18px}
.calc-btn{left:13px;top:180px;width:155px;height:29px;border-radius:15px;background:linear-gradient(#3a6fc1,#1f4d99);color:#fff;font-family:"Noto Serif",serif;font-size:14px;line-height:29px;padding-left:35px}
.calc-btn i{position:absolute;left:18px;top:8px;width:11px;height:13px;border:1.5px solid #cfdcf0;border-radius:1px}

/* cta band */
.cta{left:0;top:364px;width:798px;height:60px;background:linear-gradient(#95a2b5,#8594aa)}
.cta-text{left:116px;top:384px;font-family:"Noto Serif",serif;font-style:italic;font-size:18px;color:#fff;white-space:nowrap}
.cta-text small{font-size:10.5px}
.cta-text small b{color:var(--gold);font-weight:400}
.btn-gold{background:linear-gradient(#f0c233,var(--gold-dark));color:#fff;font-family:"Noto Serif",serif;font-weight:700;font-size:8px;text-align:center;border-radius:2px;box-shadow:0 1px 2px rgba(0,0,0,.25)}

/* main */
.main{left:0;top:424px;width:798px;height:608px;background:var(--gray-bg)}
.divider{left:489px;top:445px;width:3px;height:565px;background:#dedede}
.card{left:106px;width:367px;height:156px;background:#fff;border:1px solid #e2e2e2;box-shadow:0 1px 3px rgba(0,0,0,.12)}
.photo{left:10px;top:14px;width:77px;height:78px;background:linear-gradient(#b9cde0,#d7d3cc 40%,#8e9080 70%,#6b8a44)}
.icon-bar{left:10px;top:92px;width:77px;height:17px;background:var(--blue);display:flex}
.icon-bar svg{flex:1;height:17px}
.bid-btn{left:9px;top:117px;width:79px;height:19px;border-radius:3px;background:linear-gradient(#3a6fc1,#1f4d99);color:#fff;font-family:"Noto Serif",serif;font-size:7.4px;line-height:19px;text-align:center;white-space:nowrap}
.card-title{left:98px;top:13px;font-family:"Noto Serif",serif;font-weight:400;font-size:11.6px;color:var(--head)}
.card-desc{left:98px;top:30px;width:258px;font-size:6.3px;line-height:9.5px;color:#888}
.card-addr{left:98px;top:59px;font-size:6.6px;color:#555;display:flex;gap:5px;align-items:center}
.card-box{left:100px;top:74px;width:250px;height:62px;border:1px solid #e2e2e2}
.tabs{display:flex;height:19px;font-size:7.2px;font-weight:700;line-height:19px}
.tabs span{padding-left:8px;width:125px;white-space:nowrap}
.tabs span+span{background:#eee;color:var(--blue);font-weight:600}
.card-dates{padding:9px 0 0 8px;font-size:7.2px;line-height:13.5px;color:#333}

.pager{left:318px;top:990px;display:flex;gap:4px;align-items:center;font-size:7.4px;font-style:italic;color:#888}
.pager i{font-style:normal;width:10px;height:10px;border:1px solid #aaa;font-size:6.4px;line-height:8px;text-align:center;color:#666}
.pager i.on{background:var(--blue);border-color:var(--blue);color:#fff}

/* sidebar */
.notify{left:505px;top:446px;width:187px;height:150px;background:#e9e9e9;border:1px solid #dcdcdc}
.side-title{font-family:"Noto Serif",serif;font-weight:400;font-size:11px;color:var(--head);white-space:nowrap}
.notify .side-title{font-size:10.2px}
.email-field{left:15px;top:36px;width:160px;height:23px;background:#fff;border:1px solid #ddd;font-size:7.4px;color:#999;line-height:21px;padding-left:8px}
.notify-note{left:18px;top:68px;width:160px;font-size:7.4px;line-height:12.5px;color:#888}
.blog-item{left:505px;display:flex;gap:13px}
.thumb{width:34px;height:34px}
.blog-item p{font-size:6.8px;line-height:12px;color:#9aaac4;width:140px}
.blog-item p span{color:#666}
.person{left:513px;top:828px;width:32px;height:32px;background:linear-gradient(#cfb49a,#a8866a)}
.person-name{left:553px;top:829px;font-size:10.5px;color:#444}
.person-role{left:553px;top:845px;font-size:7.4px;color:#bbb}
.bubble{left:506px;top:878px;width:155px;height:67px;background:var(--blue);color:#fff;font-size:7.8px;line-height:15px;padding:9px 10px 0 25px;box-shadow:0 1px 2px rgba(0,0,0,.3)}
.bubble::before{content:"";position:absolute;left:12px;top:-7px;border:7px solid transparent;border-left-color:var(--blue);border-bottom-color:var(--blue);border-top:0;border-right:0}
.bubble b{position:absolute;left:9px;top:4px;font-family:"Noto Serif",serif;font-size:16px}

/* footer */
.foot-logo{left:106px;top:1056px;display:flex;align-items:center;gap:5px}
.foot-logo .logo-mark{width:18px;height:18px;border-width:3px}
.foot-logo .logo-name{font-size:11px}
.badge{background:#ececec;border:1px solid #bbb}
.foot-head{font-size:8px;font-weight:400;color:#666}
.foot-list{font-size:6.6px;line-height:15px;color:#777;list-style:none}
.foot-list li::before{content:"›";margin-right:6px;color:#999}
.contact p{font-size:6.6px;line-height:13.6px;color:#777;padding-left:16px;white-space:nowrap}
.card-mark{width:30px;height:19px;border-radius:2px;border:1px solid #ccc}
.bottom{left:0;top:1172px;width:798px;height:28px;background:var(--blue);color:#fff;font-size:6.6px;line-height:28px}
</style>
</head>
<body>

<header>
  <div class="abs logo"><span class="logo-mark"></span><span class="logo-name">The Dorlen Group</span></div>
  <div class="abs social" role="img" aria-label="Social network links">
    <span></span><span></span><span></span><span></span>
  </div>
  <p class="abs call">
    <svg width="12" height="12" viewBox="0 0 12 12" style="vertical-align:-1px"><path d="M3 1l2 2.4-1.2 1.3c.7 1.5 1.9 2.7 3.4 3.4L8.5 6.9 11 9l-1.3 1.8C5.6 10.6 1.4 6.4 1.2 2.3z" fill="none" stroke="#7b8fae" stroke-width="1"/></svg>
    Call us: <b>(555) 318-7061</b>
  </p>
</header>

<nav class="abs nav">
  <ul>
    <li style="width:57px">Home</li>
    <li class="active" style="width:57px">Auctions</li>
    <li style="width:104px">Real Estate Listings</li>
    <li style="width:51px">Rentals</li>
    <li style="width:62px">Our Team</li>
    <li style="width:55px">Services</li>
    <li style="width:76px">Past Auctions</li>
    <li style="width:73px">Testimonials</li>
    <li style="width:57px">Contact</li>
  </ul>
</nav>
<div class="abs dropdown">
  <p>›&nbsp; Auction Calendar</p>
  <p>›&nbsp; 4 Key Auction Methods</p>
  <p>›&nbsp; Auction Benefits</p>
</div>

<section class="abs hero" role="img" aria-label="Photo of a man in a cowboy hat standing in a green crop field at sunset"></section>
<h1 class="abs hero-title">The Dorlen Group will help<br>you to <em>make better decisions</em><br>in real estate.</h1>

<aside class="abs calc">
  <div class="calc-head">Mortgage Calculator</div>
  <p class="abs calc-note">Kindly enter your details below and we calculate the mortgage for you</p>
  <div class="abs field" style="left:13px;top:78px;width:84px">Amount Borrowed</div>
  <div class="abs field" style="left:101px;top:78px;width:70px">Length of Loan</div>
  <div class="abs field" style="left:13px;top:106px;width:84px">Interest Rate</div>
  <div class="abs field" style="left:101px;top:106px;width:70px">Monthly<span class="select-arrow">▲</span></div>
  <p class="abs" style="left:13px;top:143px;font-size:7.4px;color:#888">Your repayments</p>
  <div class="abs" style="left:79px;top:136px;width:92px;height:21px;background:#eee"></div>
  <div class="abs calc-btn"><i></i>Calculate Now</div>
</aside>

<section class="abs cta"></section>
<p class="abs cta-text">I am ready to sell. <small>Please contact me for a <b>FREE</b> consultation.</small></p>
<div class="abs btn-gold" style="left:522px;top:382px;width:156px;height:24px;line-height:24px">SEND AN EMAIL NOW</div>

<main class="abs main"></main>
<div class="abs divider"></div>

<article class="abs card" style="top:439px">
  <div class="abs photo" role="img" aria-label="Photo of a two-storey house"></div>
  <div class="abs icon-bar">
    <svg viewBox="0 0 25 17"><circle cx="11.5" cy="7.5" r="3" fill="none" stroke="#fff" stroke-width="1.2"/><path d="M13.7 9.7l2.5 2.5" stroke="#fff" stroke-width="1.3"/></svg>
    <svg viewBox="0 0 25 17"><rect x="8" y="5" width="9" height="7" fill="none" stroke="#fff" stroke-width="1"/><path d="M9 11l3-3 2 2 1-1 2 2" fill="none" stroke="#fff" stroke-width=".8"/></svg>
    <svg viewBox="0 0 25 17"><rect x="8" y="5.5" width="7" height="6" fill="#f0c233"/><path d="M15 8.5l3-2v4z" fill="#f0c233"/></svg>
  </div>
  <div class="abs bid-btn">View Online Bidding</div>
  <h2 class="abs card-title">Test Auction</h2>
  <p class="abs card-desc">This is a test auction, for the purposes of design and functionality testing of BidWorks.com Spark! This, of course, would be where the short description.</p>
  <p class="abs card-addr"><svg width="6" height="8" viewBox="0 0 6 8"><path d="M3 8C1 5 0 4 0 3a3 3 0 016 0c0 1-1 2-3 5z" fill="#999"/></svg>P.O. Box 40712 Fairmont, VA 24099</p>
  <div class="abs card-box"><div class="tabs"><span>ONLINE BIDDING ONLY</span><span>LIVE OFF-SITE AUCTION</span></div>
  <p class="card-dates">Begins:&nbsp; Tuesday, March 04, 2014 at 10:00 AM EST<br>Ends:&nbsp; Tuesday, March 11, 2014 at 11:00 PM EST</p></div>
</article>

<article class="abs card" style="top:616px">
  <div class="abs photo" role="img" aria-label="Photo of a two-storey house"></div>
  <div class="abs icon-bar">
    <svg viewBox="0 0 25 17"><circle cx="11.5" cy="7.5" r="3" fill="none" stroke="#fff" stroke-width="1.2"/><path d="M13.7 9.7l2.5 2.5" stroke="#fff" stroke-width="1.3"/></svg>
    <svg viewBox="0 0 25 17"><rect x="8" y="5" width="9" height="7" fill="none" stroke="#fff" stroke-width="1"/><path d="M9 11l3-3 2 2 1-1 2 2" fill="none" stroke="#fff" stroke-width=".8"/></svg>
    <svg viewBox="0 0 25 17"><rect x="8" y="5.5" width="7" height="6" fill="#f0c233"/><path d="M15 8.5l3-2v4z" fill="#f0c233"/></svg>
  </div>
  <div class="abs bid-btn">View Online Bidding</div>
  <h2 class="abs card-title">Test Auction</h2>
  <p class="abs card-desc">This is a test auction, for the purposes of design and functionality testing of BidWorks.com Spark! This, of course, would be where the short description.</p>
  <p class="abs card-addr"><svg width="6" height="8" viewBox="0 0 6 8"><path d="M3 8C1 5 0 4 0 3a3 3 0 016 0c0 1-1 2-3 5z" fill="#999"/></svg>P.O. Box 40712 Fairmont, VA 24099</p>
  <div class="abs card-box"><div class="tabs"><span>ONLINE BIDDING ONLY</span><span>LIVE OFF-SITE AUCTION</span></div>
  <p class="card-dates">Begins:&nbsp; Tuesday, March 04, 2014 at 10:00 AM EST<br>Ends:&nbsp; Tuesday, March 11, 2014 at 11:00 PM EST</p></div>
</article>

<article class="abs card" style="top:793px">
  <div class="abs photo" role="img" aria-label="Photo of a two-storey house"></div>
  <div class="abs icon-bar">
    <svg viewBox="0 0 25 17"><circle cx="11.5" cy="7.5" r="3" fill="none" stroke="#fff" stroke-width="1.2"/><path d="M13.7 9.7l2.5 2.5" stroke="#fff" stroke-width="1.3"/></svg>
    <svg viewBox="0 0 25 17"><rect x="8" y="5" width="9" height="7" fill="none" stroke="#fff" stroke-width="1"/><path d="M9 11l3-3 2 2 1-1 2 2" fill="none" stroke="#fff" stroke-width=".8"/></svg>
    <svg viewBox="0 0 25 17"><rect x="8" y="5.5" width="7" height="6" fill="#f0c233"/><path d="M15 8.5l3-2v4z" fill="#f0c233"/></svg>
  </div>
  <div class="abs bid-btn">View Online Bidding</div>
  <h2 class="abs card-title">Test Auction</h2>
  <p class="abs card-desc">This is a test auction, for the purposes of design and functionality testing of BidWorks.com Spark! This, of course, would be where the short description.</p>
  <p class="abs card-addr"><svg width="6" height="8" viewBox="0 0 6 8"><path d="M3 8C1 5 0 4 0 3a3 3 0 016 0c0 1-1 2-3 5z" fill="#999"/></svg>P.O. Box 40712 Fairmont, VA 24099</p>
  <div class="abs card-box"><div class="tabs"><span>ONLINE BIDDING ONLY</span><span>LIVE OFF-SITE AUCTION</span></div>
  <p class="card-dates">Begins:&nbsp; Tuesday, March 04, 2014 at 10:00 AM EST<br>Ends:&nbsp; Tuesday, March 11, 2014 at 11:00 PM EST</p></div>
</article>

<div class="abs pager">‹ Previous&nbsp; <i class="on">1</i><i>2</i><i>3</i><i>4</i><i>5</i><i>6</i>&nbsp; Next ›</div>

<aside class="abs notify">
  <h3 class="abs side-title" style="left:17px;top:13px">Notify me of upcoming auctions</h3>
  <div class="abs email-field">Enter Your Email *</div>
  <p class="abs notify-note">Sign up in our newsletter to get notified of specific auctions, or locations.</p>
  <div class="abs btn-gold" style="left:16px;top:102px;width:158px;height:26px;line-height:26px">SUBSCRIBE NOW</div>
</aside>

<h3 class="abs side-title" style="left:505px;top:617px">Latest Blog</h3>
<div class="abs blog-item" style="top:644px"><div class="thumb" role="img" aria-label="Blog photo of a couple" style="background:linear-gradient(#7b8794,#3c4450)"></div><p>Nunc purus orci, adipiscing non ipsum non, pellentesque fringilla sapien.<br><span>October 15, 2013</span></p></div>
<div class="abs blog-item" style="top:688px"><div class="thumb" role="img" aria-label="Blog photo of a woman" style="background:linear-gradient(#d9c8b8,#8a6a55)"></div><p>Nunc purus orci, adipiscing non ipsum non, pellentesque fringilla sapien.<br><span>October 15, 2013</span></p></div>
<div class="abs blog-item" style="top:732px"><div class="thumb" role="img" aria-label="Blog photo of a house" style="background:linear-gradient(#9cc0e0,#c9c6bd 55%,#6d8a48)"></div><p>Nunc purus orci, adipiscing non ipsum non, pellentesque fringilla sapien.<br><span>October 15, 2013</span></p></div>

<h3 class="abs side-title" style="left:505px;top:798px">Client Testimonial</h3>
<div class="abs person" role="img" aria-label="Client portrait"></div>
<p class="abs person-name">Reed Calloway</p>
<p class="abs person-role">Businessman</p>
<blockquote class="abs bubble"><b>“</b>Mauris urnaei elit, mattis non urna acem, ullamcorper ipsum dolor vula putatem lorem.</blockquote>

<footer>
  <div class="abs foot-logo"><span class="logo-mark"></span><span class="logo-name">The Dorlen Group</span></div>
  <div class="abs badge" role="img" aria-label="State auctioneers association badge" style="left:106px;top:1098px;width:58px;height:30px"></div>
  <div class="abs badge" role="img" aria-label="National auctioneers association badge" style="left:176px;top:1099px;width:22px;height:26px;background:#dfe7f4;border-color:#6a8cc8"></div>

  <h4 class="abs foot-head" style="left:243px;top:1053px">Navigation</h4>
  <ul class="abs foot-list" style="left:244px;top:1071px"><li>Home</li><li>Auctions</li><li>Real Estate Listings</li><li>Rentals</li></ul>
  <ul class="abs foot-list" style="left:333px;top:1071px"><li>Our Team</li><li>Services</li><li>Past Auctions</li><li>Testimonials</li></ul>

  <h4 class="abs foot-head" style="left:442px;top:1053px">Contact Us</h4>
  <div class="abs contact" style="left:442px;top:1072px">
    <svg class="abs" style="left:1px;top:2px" width="8" height="8" viewBox="0 0 12 12"><path d="M3 1l2 2.4-1.2 1.3c.7 1.5 1.9 2.7 3.4 3.4L8.5 6.9 11 9l-1.3 1.8C5.6 10.6 1.4 6.4 1.2 2.3z" fill="#888"/></svg>
    <svg class="abs" style="left:1px;top:31px" width="8" height="6" viewBox="0 0 8 6"><rect width="8" height="6" fill="#888"/><path d="M0 0l4 3 4-3" fill="none" stroke="#fff" stroke-width=".8"/></svg>
    <svg class="abs" style="left:2px;top:44px" width="6" height="8" viewBox="0 0 6 8"><path d="M3 8C1 5 0 4 0 3a3 3 0 016 0c0 1-1 2-3 5z" fill="#888"/></svg>
    <p>OFFICE: (555) 318-7061<br>FAX: (555) 318-7095<br>EMAIL: dgroup@vrbx.com<br>ADDRESS: 718 N. Elm Ave., Harlow NE<br>MAILING: PO Box 927, Harlow, NE</p>
  </div>

  <h4 class="abs foot-head" style="left:593px;top:1053px">We Accept</h4>
  <div class="abs card-mark" role="img" aria-label="Accepted payment card" style="left:592px;top:1073px;background:#f7f7f7"></div>
  <div class="abs card-mark" role="img" aria-label="Accepted payment card" style="left:626px;top:1073px;background:#f3e6da"></div>
  <div class="abs card-mark" role="img" aria-label="Accepted payment card" style="left:660px;top:1073px;background:var(--blue-dark);border-color:var(--blue-dark)"></div>

  <div class="abs bottom">
    <span class="abs" style="left:108px">Copyright 2014 © Dorlen Group - All Rights Reserved</span>
    <span class="abs" style="left:595px">Site Map &nbsp; • &nbsp; Privacy Policy</span>
  </div>
</footer>

</body>
</html>
```